Yoga Workshop - Yoga Practice information flyer

I am a yoga teacher who will be presenting a workshop on yoga for sleep and need a brochure for my clients which outlines a practice that I give them so they can do the practice at home. Ideally I would like a brochure that is a single A3 size of paper in size that folds in half to an A4 booklet with the entire practice on the centre section to make it easy for people to do the practice at home with just one open page in front of them:
* Front page detailing "Yoga for Sleep Workshop" and "Restorative Yoga Practice"
* Centre contains the information on the practice contained in the attached word document. The practice consists of 5 postures, so there needs to be five separate sections which have the pictures of the postures (attached in uploaded files) and the wording contained in the attached word document. All pictures uploaded need to be included in the flyer as each posture has different pictures demonstrating the posture using yoga props or using things people have at home
* Back page containing a picture of myself (picture uploaded in files) with some information about me (contained in the attached word document) and my website www.lumaverisk.com.au

I also need this flyer to be able to printed on 2 double sided A4 sheets of paper so will require 2 x pdf file versions. Importantly, for the centre section of the flyer, the design needs to ensure if it is printed on A4 paper, the wording and pictures for each of the postures are not separated over two pages

Target Market(s)

Existing clients

Requirements
Must have
• Detailed in project description
Nice to have
• The word document also contains some quotes. These do not need to be included in the flyer. If there is room and there is room for one or two of those please include where it would look good
Should not have
• Stock pictures of people in yoga postures which a normal everyday person could not get into

```html
<!DOCTYPE html>
<html lang="en">
<head>
<meta charset="utf-8">
<title>Restorative Yoga Practice – Postures 3 to 5</title>
<link rel="stylesheet" href="https://fonts.googleapis.com/css2?family=Nunito:wght@400;600;700;800&display=swap">
<style>
  :root {
    --terracotta: #d8886a;
    --navy: #2f3b57;
    --cream: #fff8f0;
    --sun: #f6d56a;
    --peach: #f2a77f;
    --photo-light: #e4d8cc;
    --photo-deep: #b98a6c;
  }
  * { box-sizing: border-box; margin: 0; padding: 0; }
  html, body { width: 849px; height: 1200px; overflow: hidden; }
  body {
    font-family: "Nunito", Arial, sans-serif;
    background: var(--terracotta);
    color: var(--cream);
  }
  .page { position: relative; width: 849px; height: 1200px; }
  .band { position: absolute; left: 0; width: 849px; }
  .band--top { top: 0; height: 398px; background: var(--terracotta); }
  .band--mid { top: 398px; height: 410px; background: var(--navy); }
  .band--bottom { top: 808px; height: 392px; background: var(--terracotta); }

  .photo {
    position: absolute;
    border: 3px solid var(--cream);
    background: linear-gradient(160deg, var(--photo-light) 0%, var(--photo-deep) 100%);
  }

  .posture { position: absolute; }
  .posture__title {
    font-weight: 800;
    font-size: 19px;
    line-height: 1.25;
    margin-bottom: 9px;
  }
  .band--mid .posture__title { color: var(--peach); }
  .posture p {
    font-size: 13.5px;
    line-height: 1.42;
    margin-bottom: 8px;
  }
  .posture p:last-child { margin-bottom: 0; }
  .label { color: var(--sun); font-weight: 700; }
</style>
</head>
<body>
<main class="page">

  <section class="band band--top">
    <div class="photo" style="left:14px; top:14px; width:134px; height:182px;" role="img" aria-label="Legs-up-the-wall pose with a bolster under the hips, view one"></div>
    <div class="photo" style="left:156px; top:14px; width:130px; height:182px;" role="img" aria-label="Legs-up-the-wall pose with a bolster under the hips, view two"></div>
    <div class="photo" style="left:14px; top:204px; width:134px; height:182px;" role="img" aria-label="Legs-up-the-wall pose using a folded blanket, view one"></div>
    <div class="photo" style="left:156px; top:204px; width:130px; height:182px;" role="img" aria-label="Legs-up-the-wall pose using a folded blanket, view two"></div>

    <article class="posture" style="left:306px; top:20px; width:525px;">
      <h2 class="posture__title">Posture 3 – Elevated Legs-Up-the-Wall Pose</h2>
      <p><span class="label">Props –</span> 1 x bolsters (or towel or blanket densely folded to a width of about 15-30cm), 1 x cushion for head support (optional)</p>
      <p><span class="label">Set up notes –</span> To enter the posture sit at 90 degrees to the wall with the side of your hip about a hand width away from the wall, and the bolster/folded towel or blanket close by. Lie down on the mat on your side then roll onto your back and extend feet up wall. The feet can push into the wall to elevate the hips slightly so the bolster/folded towel or blanket can slide underneath the hips. The prop should be positioned underneath the sacrum (flat bony structure at the base of the spine).</p>
      <p><span class="label">Caution –</span> If any lower back pain is experience adjust the height the hips are elevated by using a towel or blanket that is folded to a lower height.</p>
    </article>
  </section>

  <section class="band band--mid">
    <div class="photo" style="left:14px; top:20px; width:180px; height:218px;" role="img" aria-label="Supported child's pose over a bolster, front view"></div>
    <div class="photo" style="left:212px; top:20px; width:186px; height:218px;" role="img" aria-label="Supported child's pose over a bolster, side view"></div>
    <div class="photo" style="left:418px; top:20px; width:210px; height:218px;" role="img" aria-label="Supported child's pose over stacked pillows, side view"></div>
    <div class="photo" style="left:645px; top:20px; width:190px; height:218px;" role="img" aria-label="Supported child's pose over stacked pillows, front view"></div>

    <article class="posture" style="left:18px; top:252px; width:815px;">
      <h2 class="posture__title">Posture 4 – Supported Child's Pose</h2>
      <p><span class="label">Props –</span> 1-2 x bolsters (or 3-4 bed pillows)</p>
      <p><span class="label">Set up notes –</span> Position bolster or stacked pillows under torso. Rest the head in one direction and remember to turn to the head to the other side half way through the time you spend in this posture.</p>
      <p><span class="label">Caution –</span> If any knee or hip pain is experience, increase the height of the support under the torso by adding more bolsters, folded blankets or pillows.</p>
    </article>
  </section>

  <section class="band band--bottom">
    <div class="photo" style="left:14px; top:14px; width:134px; height:362px;" role="img" aria-label="Relaxation posture lying on back with a bolster under the knees"></div>
    <div class="photo" style="left:156px; top:14px; width:130px; height:362px;" role="img" aria-label="Relaxation posture lying on back with pillows under the knees"></div>

    <article class="posture" style="left:306px; top:24px; width:525px;">
      <h2 class="posture__title">Posture 5 – Basic Relaxation Posture with Knee Support</h2>
      <p><span class="label">Props –</span> 1 x bolsters (or 1 x bed pillow or rolled up towel)</p>
      <p><span class="label">Set up notes –</span> Reclining on back, position bolster or pillows under knees.</p>
    </article>
  </section>

</main>
</body>
</html>
```